Security Officer Training Certifications POSTCARD

We need Post Card Design
-Front and Back
-In Compliance with KOLBEX MAIL for upload!
-For Oversized and Jumbo Size Cards (kolbex mails)

Our Company:
www.northbeamlearningworks.org (FOR IDEAS)

We provide Corporate Security Officer/Criminal Justice/Police Tactics Training for Private Companies that have a security department and officers.

We provide:
Handcuffing certifications
Pepper Spray
Compliance Training
Instructor Training
California Guard Card

FRONT DESIGN TO BE VERY CATCH!
Back of Card List of Services/Menu

Our Card to display powerful image for a Security Officer Department
Traits in Pic and Deigns
VALUE
COMPETITIVE EDGE
PROFESSIONAL GROWTH
QUALITY
PROFICIENT/EFFECTIVE SECURITY OFFICERS
TACTICAL OFFICERS
PROFESSIONALISM
EXPERTS
INDUSTRY LEADERS
READINESS

Target Market(s)

Proprietary Security Officer Department. Agencies that hire their own guard force.
It will be owners of security guard companies, Security Directors, manager

Industry/Entity Type

Security

Requirements
Must have
• GREAT FROM OF CARD PICTURE that encompasses
• Corporate Security Officers
• MUST HAVE A COOL LOOK!
• Professionalism
• Tactical
• The best
• Upgrade skills
• BACK of Card:
• Like list of services with pics and cool stuff
• PICS of Security Officer /Police Professionals
• with great backgrounds!
• COOL
• BACK OF CARD
• Space to have address of receipient
• space for post age
• in ACCORDANCE with KOLBEX MAILS to upload...

```html
<!DOCTYPE html>
<html lang="en">
<head>
<meta charset="utf-8">
<title>Northbeam Learning Works – Security Training Postcard</title>
<link rel="stylesheet" href="https://fonts.googleapis.com/css2?family=Lato:ital,wght@0,400;0,700;0,900;1,400;1,700;1,900&family=Roboto+Condensed:wght@700&family=Roboto:wght@500;700&family=Roboto+Slab:wght@700&display=swap">
<style>
  :root {
    --red: #9c1b20;
    --red-deep: #7f1418;
    --blue: #2b3591;
    --blue-text: #27308a;
    --ink: #2b2b2b;
    --dark-box: #333333;
    --paper: #ffffff;
    --canvas: #e6e6e6;
    --stamp: #dedede;
    --curve-gray: #cfcfcf;
  }
  * { margin: 0; padding: 0; box-sizing: border-box; }
  html, body { width: 825px; height: 1200px; overflow: hidden; }
  body { background: var(--canvas); position: relative; font-family: "Lato", sans-serif; }

  .postcard { position: absolute; left: 96px; width: 634px; height: 410px; background: var(--paper); overflow: hidden; }
  .postcard--front { top: 174px; }
  .postcard--back { top: 655px; }
  .postcard svg.shapes { position: absolute; inset: 0; }
  .abs { position: absolute; }

  /* front */
  .front-heading { left: 0; top: 20px; width: 360px; text-align: center; color: var(--paper); line-height: 1.1; }
  .front-heading .line-a, .front-heading .line-c { font-family: "Roboto", sans-serif; font-weight: 700; font-size: 16px; letter-spacing: .2px; }
  .front-heading .line-b { font-family: "Roboto Condensed", sans-serif; font-weight: 700; font-size: 18px; margin: 2px 0; }
  .front-heading .line-c { font-size: 17.5px; }
  .program-title { color: var(--red); font-style: italic; font-weight: 900; font-size: 19px; }
  .contact-line { color: var(--blue-text); font-style: italic; font-weight: 900; font-size: 25px; letter-spacing: -.2px; }
  .offer-box { left: 30px; top: 274px; width: 312px; height: 82px; background: var(--dark-box); border: 3px solid var(--red); border-bottom: none; border-radius: 14px 14px 0 0; color: var(--paper); text-align: center; padding-top: 16px; }
  .offer-box .offer-main { font-family: "Roboto Slab", serif; font-weight: 700; font-size: 17px; }
  .offer-box .offer-sub { font-family: "Roboto", sans-serif; font-weight: 700; font-size: 16px; margin-top: 4px; }
  .instructor-note { right: 28px; top: 273px; width: 268px; text-align: right; font-style: italic; font-size: 9.4px; line-height: 1.28; color: var(--ink); }
  .site-line { left: 0; bottom: 0; width: 100%; height: 47px; line-height: 47px; text-align: center; color: var(--paper); font-size: 17px; letter-spacing: 1.4px; }

  /* back */
  .back-tagline { left: 36px; top: 32px; color: var(--paper); font-style: italic; font-weight: 700; font-size: 14px; line-height: 1.4; }
  .back-program { left: 30px; top: 128px; }
  .back-contact { left: 30px; top: 154px; font-size: 27px; }
  .back-permits { left: 33px; top: 194px; font-family: "Roboto", sans-serif; font-weight: 700; font-size: 22px; color: var(--ink); }
  .service-list { left: 40px; top: 279px; list-style: none; color: var(--paper); font-style: italic; font-weight: 700; font-size: 16px; line-height: 22px; }
  .service-list li::before { content: "●"; font-style: normal; font-size: 12px; margin-right: 8px; position: relative; top: -1px; }
  .brand-mark { left: 292px; top: 258px; width: 74px; text-align: center; color: var(--paper); font-weight: 700; font-size: 9px; line-height: 1.15; }
  .brand-mark .dot { width: 40px; height: 40px; border: 2px solid var(--paper); border-radius: 50%; margin: 0 auto 5px; }
  .stamp-box { left: 545px; top: 26px; width: 59px; height: 59px; background: var(--stamp); }
</style>
</head>
<body>

<section class="postcard postcard--front">
  <svg class="shapes" width="634" height="410" viewBox="0 0 634 410">
    <defs>
      <linearGradient id="fadeFloor" x1="0" y1="0" x2="0" y2="1">
        <stop offset="0" stop-color="#ffffff"/><stop offset="1" stop-color="#e9e9e9"/>
      </linearGradient>
      <linearGradient id="officerTone" x1="0" y1="0" x2="1" y2="1">
        <stop offset="0" stop-color="#a9c6e6"/><stop offset=".55" stop-color="#3d4a66"/><stop offset="1" stop-color="#1c2233"/>
      </linearGradient>
      <linearGradient id="smallTone" x1="0" y1="0" x2="0" y2="1">
        <stop offset="0" stop-color="#c9cfd8"/><stop offset="1" stop-color="#3a3f4a"/>
      </linearGradient>
    </defs>
    <rect x="0" y="0" width="634" height="410" fill="url(#fadeFloor)"/>
    <path d="M0 0 H420 V112 Q300 138 0 126 Z" fill="var(--red)"/>
    <path d="M0 126 Q300 138 420 112 V120 Q300 150 0 140 Z" fill="#f3f3f3"/>
    <circle cx="504" cy="112" r="136" fill="var(--red)"/>
    <circle cx="504" cy="112" r="130" fill="url(#officerTone)" role="img" aria-label="Photo of a uniformed officer aiming a handgun"/>
    <g stroke="var(--red)" stroke-width="4">
      <circle cx="69" cy="151" r="40" fill="url(#smallTone)" role="img" aria-label="Photo of officers in a dark training room"/>
      <circle cx="174" cy="151" r="40" fill="url(#smallTone)" role="img" aria-label="Photo of a security officer on patrol"/>
      <circle cx="279" cy="151" r="40" fill="#b8965a" role="img" aria-label="Photo of an officer at a firing range"/>
    </g>
    <rect x="0" y="354" width="634" height="3" fill="var(--red)"/>
    <rect x="0" y="363" width="634" height="47" fill="var(--blue)"/>
  </svg>

  <div class="abs front-heading">
    <div class="line-a">SECURITY CORPORATE TRAINING</div>
    <div class="line-b">ON-SITE – SEMINARS – GROUP SETTINGS</div>
    <div class="line-c">REGULATORY &amp; COMPLIANCE</div>
  </div>
  <div class="abs program-title" style="left:37px;top:206px;">On-Site Instructor Training Program</div>
  <div class="abs contact-line" style="left:37px;top:229px;">Contact us at: 555-014-2290</div>
  <div class="abs offer-box">
    <div class="offer-main">50% OFF Security Academy</div>
    <div class="offer-sub">Get ALL Permits Only $187.50</div>
  </div>
  <p class="abs instructor-note">Get Recognized as a Handcuffing Instructor. Get all the tools you need to have a successful training program! Be able to train others! *FREE Instructor Power Points, Student Manuals, Forms, Certificate &amp; Pocket license ISSUE YOUR STUDENTS GCB certified training!</p>
  <div class="abs site-line">Visit us at: www.northbeamlearningworks.org</div>
</section>

<section class="postcard postcard--back">
  <svg class="shapes" width="634" height="410" viewBox="0 0 634 410">
    <path d="M384 0 Q445 150 424 410 H436 Q458 150 396 0 Z" fill="var(--curve-gray)"/>
    <path d="M0 0 H384 Q400 45 410 95 H0 Z" fill="var(--red)"/>
    <path d="M0 242 H422 Q423 300 422 355 H275 V410 H0 Z" fill="var(--blue)"/>
  </svg>

  <p class="abs back-tagline">On-Site – We come to you – SAVE on Staff<br>Training with our compliance &amp; training Seminars</p>
  <div class="abs program-title back-program">On-Site Instructor Training Program</div>
  <div class="abs contact-line back-contact">Contact us at: 555-014-2290</div>
  <div class="abs back-permits">Get ALL Permits Only $187.50</div>
  <ul class="abs service-list">
    <li>Handcuffing certifications</li>
    <li>Pepper Spray</li>
    <li>Compliance Training</li>
    <li>Instructor Training</li>
    <li>California Guard Card</li>
  </ul>
  <div class="abs brand-mark">
    <div class="dot"></div>
    Northbeam Learning Works
  </div>
  <div class="abs stamp-box"></div>
</section>

</body>
</html>
```